Automotive component supplier needs a business card design

We need a business card design for our company called Vexlo Global Fittings Ltd based in the UK. We are a supplier of interior and exterior components to premium car manufacturers such as Harwick Vale, Denby Stroud, Calloway and Ferrucatti. We would like to see a modern business card design that uses the colour blue.

Target Market(s)

Premium automotive car manufacturers.

Industry/Entity Type

Automotive

Contact Information for Business Card

Company Name : Vexlo Global Fittings Limited
Address: 17 Tamsin Yard, Upper Heath, Warwick, CV32 8LN, United Kingdom
Web Address : www.vexlofittings-demo.co.uk

Font styles to use
Other font styles liked:
• Helvetica

Colors
3176b5
0255a3
85acd3
cfdeed
cee9f5
85cae6
34a6d7
0692cd
9bcb3c

Requirements
Must have
• Clear company logo and a mixture of blue colours.
Nice to have
• A high quality modern image.
Should not have
• Multiple colours.

```html
<!DOCTYPE html>
<html lang="en">
<head>
<meta charset="utf-8">
<title>Vexlo Global Fittings – Business Card</title>
<link rel="stylesheet" href="https://fonts.googleapis.com/css2?family=Arimo:wght@400;700&family=Open+Sans:wght@400;600&family=Oswald:wght@600&display=swap">
<style>
  :root {
    --page-bg: #eeeeee;
    --blue-deep: #0255a3;
    --blue-mid: #3176b5;
    --blue-bright: #0692cd;
    --blue-sky: #34a6d7;
    --blue-light: #85cae6;
    --blue-ice: #cee9f5;
    --paper: #ffffff;
    --ink-blue: #1c4f9c;
  }
  html, body {
    margin: 0;
    padding: 0;
    width: 1193px;
    height: 1200px;
    overflow: hidden;
    background: var(--page-bg);
  }
  .sheet {
    width: 1193px;
    height: 1200px;
    display: flex;
    flex-direction: column;
    align-items: center;
    justify-content: space-evenly;
  }
  .card {
    display: block;
    width: 900px;
    height: 540px;
    box-shadow: 0 6px 18px rgba(0,0,0,0.18);
  }
  .brand-name { font-family: "Arimo", sans-serif; font-weight: 700; }
  .brand-tag { font-family: "Arimo", sans-serif; font-weight: 400; letter-spacing: 0.6px; }
  .person-name { font-family: "Oswald", sans-serif; font-weight: 600; fill: var(--ink-blue); }
  .person-role { font-family: "Oswald", sans-serif; font-weight: 600; fill: var(--ink-blue); }
  .contact-line { font-family: "Open Sans", sans-serif; font-weight: 400; fill: var(--blue-deep); }
  .contact-icon { fill: var(--blue-deep); }
</style>
</head>
<body>
<main class="sheet">

  <!-- Front of card -->
  <svg class="card card-front" viewBox="0 0 372 223" xmlns="http://www.w3.org/2000/svg">
    <defs>
      <linearGradient id="front-top" x1="0" y1="0" x2="1" y2="1">
        <stop offset="0" stop-color="var(--blue-sky)"/>
        <stop offset="0.6" stop-color="#2ea0d4"/>
        <stop offset="1" stop-color="var(--blue-bright)"/>
      </linearGradient>
      <linearGradient id="front-bottom" x1="0" y1="0" x2="1" y2="0">
        <stop offset="0" stop-color="#2f86c6"/>
        <stop offset="0.55" stop-color="#3b8fcf"/>
        <stop offset="1" stop-color="var(--blue-mid)"/>
      </linearGradient>
      <linearGradient id="front-white-shade" x1="0" y1="0" x2="0" y2="1">
        <stop offset="0" stop-color="#ffffff"/>
        <stop offset="1" stop-color="#e9eef2"/>
      </linearGradient>
    </defs>
    <rect class="band-top" x="0" y="0" width="372" height="81" fill="url(#front-top)"/>
    <rect class="band-white" x="0" y="81" width="372" height="77" fill="url(#front-white-shade)"/>
    <rect class="band-bottom" x="0" y="158" width="372" height="65" fill="url(#front-bottom)"/>
    <text class="brand-name" x="176" y="126" text-anchor="middle" font-size="34" fill="var(--blue-bright)">VEXLO</text>
    <text class="brand-tag" x="186" y="142" text-anchor="middle" font-size="8.6" fill="var(--blue-bright)">GLOBAL FITTINGS</text>
  </svg>

  <!-- Back of card -->
  <svg class="card card-back" viewBox="0 0 372 223" xmlns="http://www.w3.org/2000/svg">
    <defs>
      <linearGradient id="back-base" x1="0" y1="0" x2="1" y2="1">
        <stop offset="0" stop-color="var(--blue-sky)"/>
        <stop offset="0.5" stop-color="#2b8fcf"/>
        <stop offset="1" stop-color="var(--blue-mid)"/>
      </linearGradient>
      <radialGradient id="back-glow" cx="0.52" cy="0.58" r="0.28">
        <stop offset="0" stop-color="var(--blue-ice)" stop-opacity="0.85"/>
        <stop offset="0.4" stop-color="var(--blue-light)" stop-opacity="0.45"/>
        <stop offset="1" stop-color="var(--blue-light)" stop-opacity="0"/>
      </radialGradient>
    </defs>
    <rect x="0" y="0" width="372" height="223" fill="url(#back-base)"/>
    <rect x="0" y="0" width="372" height="223" fill="url(#back-glow)"/>

    <!-- Logo -->
    <text class="brand-name" x="30" y="52" font-size="24" fill="var(--paper)">VEXLO</text>
    <text class="brand-tag" x="30" y="60" font-size="5.4" fill="var(--paper)">GLOBAL FITTINGS</text>

    <!-- Name panel -->
    <polygon class="name-panel" points="222,0 372,0 372,76 202,74" fill="var(--paper)" stroke="var(--blue-deep)" stroke-width="1"/>
    <text class="person-name" x="287" y="46" text-anchor="middle" font-size="14">MR. ALDEN MARSH</text>
    <text class="person-role" x="287" y="59" text-anchor="middle" font-size="9.5">Managing Director</text>

    <!-- Contact panel -->
    <polygon class="contact-panel" points="0,105 137,105 307,223 0,223" fill="var(--paper)"/>
    <polyline points="0,105 137,105 307,223" fill="none" stroke="var(--blue-deep)" stroke-width="1.2"/>

    <!-- phone -->
    <path class="contact-icon" d="M31 114.5c.6-.6 1.3-.6 1.7 0l1 1.2c.3.4.2.9-.2 1.2l-.5.4c.4.9 1.2 1.8 2.1 2.2l.4-.5c.3-.4.8-.5 1.2-.2l1.2 1c.5.4.5 1.1 0 1.6-.9.9-2.4 1-4 0-1.6-1-2.8-2.3-3.4-3.9-.4-1.2-.2-2.3.5-3z"/>
    <text class="contact-line" x="48" y="121" font-size="8.2">020-7946-0183</text>

    <!-- envelope -->
    <rect class="contact-icon" x="31" y="137" width="8" height="6" rx="0.5"/>
    <polyline points="31.3,137.5 35,140.6 38.7,137.5" fill="none" stroke="var(--paper)" stroke-width="0.8"/>
    <text class="contact-line" x="48" y="143" font-size="8.2">contact@vexlofittings-demo.co.uk</text>

    <!-- globe -->
    <circle class="contact-icon" cx="35" cy="162" r="4"/>
    <ellipse cx="35" cy="162" rx="1.7" ry="4" fill="none" stroke="var(--paper)" stroke-width="0.6"/>
    <line x1="31" y1="162" x2="39" y2="162" stroke="var(--paper)" stroke-width="0.6"/>
    <text class="contact-line" x="48" y="165" font-size="8.2">www.vexlofittings-demo.co.uk</text>

    <!-- home -->
    <path class="contact-icon" d="M35 181l4.5 4h-1.3v4h-2.3v-2.6h-1.8v2.6h-2.3v-4h-1.3z"/>
    <text class="contact-line" x="48" y="186" font-size="8.2">17 Tamsin Yard, Upper Heath,</text>
    <text class="contact-line" x="48" y="195" font-size="8.2">Warwick, CV32 8LN, United Kingdom</text>
  </svg>

</main>
</body>
</html>
```